A5 Flyer for Window Cleaning Company

2 sided Flyer design required for window cleaning company. One side to include we use traditional and hot water fed pole window cleaning systems, conservatory cleaning, and fascia and soffit cleaning. The other side to be for Gutter cleaning. See the must haves section of project brief for more info. Mixture of some images and text for both sides. ( do not have to use all images supplied). The flyer will be used to promote the business to new residential customers.

Target Market(s)

Private households/new customers

Industry/Entity Type

Window Cleaning

Font styles to use
Serif

Requirements
Must have
• Company address ( 7 Old Pennick Court Harlow Street Edinburgh EH4 9RQ
Phone numbers( 0131 482 7719 0800 061 2287).
Website and email address ( info@falconbright-cleaning.example)
Excellent Customer Service. Competitive prices. Established 1994.
Side 1of flyer = Falconbright Window Cleaning Side 2 of flyer Falconbright Gutter Cleaning.
Nice to have
• Professional look.

```html
<!DOCTYPE html>
<html lang="en">
<head>
<meta charset="utf-8">
<title>Falconbright Cleaning Flyers</title>
<link href="https://fonts.googleapis.com/css2?family=Oswald:wght@500;600&family=Nunito+Sans:wght@400;700;800&display=swap" rel="stylesheet">
<style>
:root{
  --stage:#6a6a6a;
  --navy:#2b2a78;
  --navy-deep:#23226a;
  --blue:#1f7fd0;
  --blue-light:#3a9be0;
  --ink:#22224e;
  --text:#2a2a2a;
  --paper:#f5f6fa;
  --white:#ffffff;
  --gold:#d8a928;
}
*{box-sizing:border-box;margin:0;padding:0}
html,body{width:1200px;height:843px;overflow:hidden}
body{background:var(--stage);font-family:"Nunito Sans",Arial,sans-serif;position:relative}
.flyer{position:absolute;top:66px;width:500px;height:709px;background:var(--paper);overflow:hidden;box-shadow:0 6px 18px rgba(0,0,0,.35)}
.flyer--window{left:70px}
.flyer--gutter{left:626px}
.abs{position:absolute}
.hero{left:0;top:0;width:500px;height:270px}
.hero--window{background:linear-gradient(120deg,#9aa6ad 0%,#c9d3d8 35%,#4f7f9f 55%,#7b8c5a 100%)}
.hero--gutter{background:linear-gradient(135deg,#5b5f66 0%,#8e939a 40%,#c08a3a 60%,#e6e8ea 100%)}
.band{left:0;top:176px;width:500px;height:180px;background:var(--navy);clip-path:polygon(0 14%,60% 0,100% 0,100% 100%,0 100%)}
.thumb{top:182px;width:136px;height:78px;border:3px solid #8e8fb8}
.thumb--a{left:32px}.thumb--b{left:182px}.thumb--c{left:332px}
.brand{left:372px;top:27px;width:94px;height:108px;background:var(--white);display:flex;flex-direction:column;align-items:center;justify-content:center;gap:6px;padding:6px}
.brand__mark{width:22px;height:22px;background:var(--navy)}
.brand__name{font-family:"Oswald",sans-serif;font-weight:600;color:var(--navy);font-size:14px;text-align:center;line-height:1.1}
.title{left:0;width:500px;text-align:center;font-family:"Oswald",sans-serif;font-weight:600;color:var(--white);letter-spacing:.5px;line-height:1}
.flyer--window .title{top:263px;font-size:33px}
.flyer--gutter .title{top:278px;font-size:33px}
.strip{left:0;top:329px;width:500px;height:20px;background:var(--blue)}
.subtitle{left:82px;top:308px;width:336px;height:30px;background:var(--blue);clip-path:polygon(8% 0,92% 0,100% 100%,0 100%);color:var(--white);font-family:"Oswald",sans-serif;font-weight:500;font-size:19px;text-align:center;line-height:32px}
.tagline{left:35px;top:341px;width:430px;height:26px;border-radius:13px;background:var(--navy);color:var(--white);font-weight:800;font-size:11.5px;text-align:center;line-height:26px}
.flyer--gutter .tagline{top:325px;left:35px;background:var(--blue-light)}
.flyer--gutter .band{height:175px}
.lead{left:39px;top:378px;width:200px;color:var(--navy);font-weight:800;font-size:11.5px;line-height:1.1}
.lead-box{left:39px;top:393px;width:210px;height:44px;background:var(--navy);color:var(--white);padding:3px 10px}
.lead-box b{display:block;font-family:"Oswald",sans-serif;font-weight:500;font-size:17px;line-height:1.2}
.lead-box span{display:block;font-weight:800;font-size:11px}
.lead--more{top:441px}
.copy{left:39px;top:486px;width:192px;font-size:7.6px;line-height:1.5;color:var(--text);text-align:justify}
.copy p{margin-bottom:3px}
.guarantee{left:274px;top:381px;width:192px;font-size:7.6px;line-height:1.5;color:var(--text);text-align:justify}
.guarantee strong{font-size:11px;color:var(--ink)}
.guarantee em{font-style:normal;font-size:12px;color:var(--blue);font-weight:800}
.van{left:250px;top:458px;width:212px;height:130px;border-radius:10px;background:linear-gradient(160deg,#d9ecfa,#4aa5e3 70%,#2f6fae)}
.seal{left:423px;top:590px;width:42px;height:42px;border-radius:50%;background:var(--gold)}
.footer{left:0;top:613px;width:500px;height:96px;background:var(--blue);clip-path:polygon(0 0,52% 0,58% 33%,100% 33%,100% 100%,0 100%)}
.footer-line{left:254px;top:613px;width:34px;height:3px;background:var(--navy);transform-origin:0 0;transform:rotate(47deg)}
.contact{left:40px;color:var(--white);display:flex;align-items:center;gap:6px}
.contact svg{width:11px;height:11px;flex:none}
.contact--phone{font-weight:800;font-size:14px}
.contact--mail{font-size:11px}
.c1{top:621px}.c2{top:640px}.c3{top:662px}.c4{top:679px}
.address{left:318px;top:663px;color:var(--white);font-size:10.5px;line-height:1.3;display:flex;gap:5px}
.address svg{width:9px;height:11px;flex:none;margin-top:1px}
.panel-head{top:366px;height:28px;background:var(--navy);color:var(--white);font-family:"Oswald",sans-serif;font-weight:500;font-size:18px;line-height:28px;padding-left:18px}
.panel-head--services{left:39px;width:208px}
.panel-head--about{left:268px;width:200px}
.services-intro{left:39px;top:400px;width:210px;color:var(--navy);font-size:10px;line-height:1.25}
.service-list{left:39px;top:444px;width:210px;list-style:none}
.service-list li{display:flex;align-items:center;gap:6px;color:var(--ink);font-weight:800;font-size:11.5px;height:19.2px}
.service-list svg{width:9px;height:9px;flex:none}
.services-outro{left:39px;top:564px;width:210px;font-size:7.6px;line-height:1.45;color:var(--text);text-align:justify}
.about-sub{left:268px;top:400px;color:var(--blue);font-weight:800;font-size:10.5px}
.about-list{left:268px;top:416px;width:200px;font-size:7.6px;line-height:1.5;color:var(--text)}
.about-list p{margin-bottom:4px;text-align:justify}
.about-list b{color:var(--blue);font-weight:800}
.badge{top:604px;height:24px;background:#cfd3dc}
.badge--1{left:295px;width:64px;border-radius:3px}
.badge--2{left:381px;width:24px}
.badge--3{left:426px;width:26px;border-radius:50%}
</style>
</head>
<body>
<svg width="0" height="0" style="position:absolute">
  <defs>
    <symbol id="i-phone" viewBox="0 0 24 24"><circle cx="12" cy="12" r="10.5" fill="none" stroke="#fff" stroke-width="2"/><path d="M8.5 7l2 2.2-1 1.3c.8 1.7 2 2.9 3.6 3.7l1.3-1 2.1 2-1.2 1.6c-3.8-.6-7.7-4.4-8.2-8.3z" fill="#fff"/></symbol>
    <symbol id="i-mail" viewBox="0 0 24 24"><rect x="2" y="5" width="20" height="14" fill="none" stroke="#fff" stroke-width="2"/><path d="M2 5l10 8 10-8" fill="none" stroke="#fff" stroke-width="2"/></symbol>
    <symbol id="i-web" viewBox="0 0 24 24"><circle cx="12" cy="12" r="10" fill="none" stroke="#fff" stroke-width="2"/><path d="M2 12h20M12 2c3.5 3.5 3.5 16.5 0 20M12 2c-3.5 3.5-3.5 16.5 0 20" fill="none" stroke="#fff" stroke-width="1.6"/></symbol>
    <symbol id="i-pin" viewBox="0 0 20 24"><path d="M10 1a7 7 0 0 1 7 7c0 5-7 14-7 14S3 13 3 8a7 7 0 0 1 7-7z" fill="none" stroke="#fff" stroke-width="2"/><circle cx="10" cy="8" r="2.5" fill="#fff"/></symbol>
    <symbol id="i-tick" viewBox="0 0 24 24"><circle cx="12" cy="12" r="10" fill="none" stroke="#1f7fd0" stroke-width="2.4"/><path d="M7 12.5l3.2 3.2L17 9" fill="none" stroke="#1f7fd0" stroke-width="2.4"/></symbol>
  </defs>
</svg>

<!-- Side 1: window cleaning -->
<article class="flyer flyer--window">
  <div class="abs hero hero--window" role="img" aria-label="Window cleaner in a blue cap and shirt wiping a large glass pane with a squeegee"></div>
  <div class="abs band"></div>
  <div class="abs thumb thumb--a" style="background:linear-gradient(135deg,#4f86b5,#b04056)" role="img" aria-label="Cleaner working on a glass shopfront"></div>
  <div class="abs thumb thumb--b" style="background:linear-gradient(135deg,#e8ecef,#9aa5ad)" role="img" aria-label="Water fed pole brush cleaning a conservatory roof"></div>
  <div class="abs thumb thumb--c" style="background:linear-gradient(135deg,#4f8a3c,#8a4a38)" role="img" aria-label="Cleaner on a ladder at a brick house gable"></div>
  <div class="abs brand"><span class="brand__mark"></span><span class="brand__name">Falconbright</span></div>
  <h1 class="abs title">FALCONBRIGHT WINDOW CLEANING</h1>
  <div class="abs strip"></div>
  <div class="abs subtitle">NEW HOT WATER FED POLE SYSTEM</div>
  <div class="abs tagline">Excellent Customer Service. Competitive prices. Established 1994.</div>

  <p class="abs lead">WE USE TRADITIONAL AND</p>
  <div class="abs lead-box"><b>NEW HOT WATER FED POLE</b><span>WINDOW CLEANING SYSTEMS,</span></div>
  <p class="abs lead lead--more">CONSERVATORY CLEANING,<br>AND FASCIA AND<br>SOFFIT CLEANING.</p>
  <div class="abs copy">
    <p>Established since 1995, we have built up a reliable and trusted Falconbright Window Cleaning reputation on the west side of Edinburgh.</p>
    <p>We specialise in serving the needs of homes that want the highest standards of cleaning at very competitive rates. As a result, a high percentage of our business is from repeat customers and referrals.</p>
    <p>All our staff are uniformed and carry Identification Cards at all times.</p>
  </div>
  <p class="abs guarantee"><strong>WE OFFER </strong><em>100% GUARANTEE</em> on our workmanship. If however our standards do not meet your expectations, please phone or email within 2 days of having your windows cleaned and we will come back and clean them again at no extra cost.</p>
  <div class="abs van" role="img" aria-label="Branded company van with ladders on the roof rack"></div>
  <div class="abs seal"></div>

  <div class="abs footer"></div>
  <div class="abs footer-line"></div>
  <div class="abs contact contact--phone c1"><svg><use href="#i-phone"/></svg>0131 482 7719</div>
  <div class="abs contact contact--phone c2"><svg><use href="#i-phone"/></svg>0800 061 2287</div>
  <div class="abs contact contact--mail c3"><svg><use href="#i-mail"/></svg>info@falconbright-cleaning.example</div>
  <div class="abs contact contact--mail c4"><svg><use href="#i-web"/></svg>falconbright-cleaning.example</div>
  <div class="abs address"><svg><use href="#i-pin"/></svg><span>7 Old Pennick Court<br>Harlow Street<br>Edinburgh EH4 9RQ</span></div>
</article>

<!-- Side 2: gutter cleaning -->
<article class="flyer flyer--gutter">
  <div class="abs hero hero--gutter" role="img" aria-label="Gloved hand lifting autumn leaves out of a roof gutter"></div>
  <div class="abs band"></div>
  <div class="abs thumb thumb--a" style="top:193px;background:linear-gradient(135deg,#b5603e,#e9eef2)" role="img" aria-label="Brick house with a white conservatory"></div>
  <div class="abs thumb thumb--b" style="top:193px;background:linear-gradient(135deg,#f4f4f4,#b9bcc0)" role="img" aria-label="Labelled diagram of fascia, soffit, guttering and down pipe"></div>
  <div class="abs thumb thumb--c" style="top:193px;background:linear-gradient(135deg,#4f8a3c,#8a4a38)" role="img" aria-label="Cleaner on a ladder at a brick house gable"></div>
  <div class="abs brand"><span class="brand__mark"></span><span class="brand__name">Falconbright</span></div>
  <h1 class="abs title">FALCONBRIGHT GUTTER CLEANING</h1>
  <div class="abs tagline">Excellent Customer Service. Competitive prices. Established 1994.</div>

  <h2 class="abs panel-head panel-head--services">OUR SERVICES</h2>
  <p class="abs services-intro">With our new Water Fed Pole system we can offer you even more services and benefits to those listed below:-</p>
  <ul class="abs service-list">
    <li><svg><use href="#i-tick"/></svg>Exterior Window Cleaning</li>
    <li><svg><use href="#i-tick"/></svg>Gutter And Rhone Cleaning</li>
    <li><svg><use href="#i-tick"/></svg>Fascia And Soffit Cleaning</li>
    <li><svg><use href="#i-tick"/></svg>Conservatory Cleaning</li>
    <li><svg><use href="#i-tick"/></svg>One-off Cleans</li>
    <li><svg><use href="#i-tick"/></svg>Builders Cleans</li>
  </ul>
  <p class="abs services-outro">We would welcome the opportunity to earn your trust and deliver you the best Edinburgh window cleaning service in the industry.</p>

  <h2 class="abs panel-head panel-head--about">ABOUT US</h2>
  <p class="abs about-sub">Reasons to choose us.</p>
  <div class="abs about-list">
    <p><b>QUALITY</b> - We ensure the highest standards of window cleaning work and offer 100% guarantee on all of our work</p>
    <p><b>COMPETITIVE</b> - Fair Pricing &amp; Free Estimates</p>
    <p><b>PROFESSIONAL</b> - Trained, Uniformed and Insured Window Cleaners</p>
    <p><b>INSURANCE</b> - We have full public and employers liability insurance</p>
    <p><b>EXPERIENCED</b> - Established in 1995, we have over 20 years experience of serving our clients</p>
    <p><b>FRIENDLY</b> - Established, Helpful and Polite Customer Service</p>
    <p><b>LICENSED and REGULATED</b> by City of Edinburgh Council</p>
  </div>

  <div class="abs footer"></div>
  <div class="abs footer-line"></div>
  <div class="abs badge badge--1"></div>
  <div class="abs badge badge--2"></div>
  <div class="abs badge badge--3"></div>
  <div class="abs contact contact--phone c1"><svg><use href="#i-phone"/></svg>0131 482 7719</div>
  <div class="abs contact contact--phone c2"><svg><use href="#i-phone"/></svg>0800 061 2287</div>
  <div class="abs contact contact--mail c3"><svg><use href="#i-mail"/></svg>info@falconbright-cleaning.example</div>
  <div class="abs contact contact--mail c4"><svg><use href="#i-web"/></svg>falconbright-cleaning.example</div>
  <div class="abs address"><svg><use href="#i-pin"/></svg><span>7 Old Pennick Court<br>Harlow Street<br>Edinburgh EH4 9RQ</span></div>
</article>
</body>
</html>
```